Esoteric, wellness company labels

Verdant Lumen is a lifestyle brand with multiple products. We have an offshoot as well called Lumen Coffee. I need multiple labels or packaging designs that all match so I can start wholesaling.

I want something fun and very eye catching. I have two different logos for Verdant Lumen but just one for the coffee. I’m
Undecided which one I want on the labels because I like both. So either would work. Any coffee products go under lumen coffee and any other products go under Verdant Lumen.

We sell items such as crystals, tarot and oracle decks, candles, organic coffee, superfood powders and herbs and more.

The items I need labels for should have a streamline look so that all are recognizable as the Verdant Lumen brand. The products that are a priority are:
Organic coffee
Reishi infused coffee
Lion’s Mane infused coffee
Those go under Lumen Coffee.

Soon I’ll do more items;
Sacred smudging spray
Sacred smudging cleaner
Multiple superfoods
Etc
Updates

We have decided to use compostable coffee bags that are approximately 9x6x33cm so your standard 1lb bag you would see in a store. We still want colorful and eye catching but at the same time being eco friendly. The coffee is 100% organic, free trade, low acid.

We are looking for labels for the coffee but also want to be able to use the same kind of design or similar down the road for our other products. We carry superfood powders (lion’s mane, blue Spirulina, reishi, pearl powder, sea moss etc) but also things like smudging spray, rose water, neroli water, essential oils etc. we are a lifestyle company so we are looking for labels across our store brand items.

Target Market(s)

Esoteric, health and wellness, “new age”

Industry/Entity Type

Retail, wellness,

Colors

Designer to choose colors to be used in the design.

Requirements
Must have
• Beauty, attraction
Should not have
• Anything to do with religion, no dark witchy themes

```html
<!DOCTYPE html>
<html lang="en">
<head>
<meta charset="utf-8">
<title>Lumen Coffee — Label Options</title>
<link rel="stylesheet" href="https://fonts.googleapis.com/css2?family=Titan+One&family=Oswald:wght@400;600&family=Poiret+One&family=Josefin+Sans:wght@300;400&display=swap">
<style>
  :root {
    --page: #f4f4f2;
    --caption: #1d1d1d;
    --roast: #3a2117;
    --amber: #e39a3b;
    --tan: #d9b07a;
    --cream: #f6ead4;
    --teal: #4e8a80;
    --navy: #263c45;
    --gold: #e7c98f;
    --ember: #d2673e;
  }
  * { box-sizing: border-box; margin: 0; padding: 0; }
  html, body { width: 849px; height: 1200px; overflow: hidden; background: var(--page); }
  .sheet { position: relative; width: 849px; height: 1200px; }

  .option { position: absolute; left: 0; width: 849px; height: 560px; }
  .option--three { top: 20px; }
  .option--four { top: 610px; }

  .option__caption {
    position: absolute; right: 52px; bottom: 18px;
    font: 600 16px "Oswald", sans-serif; color: var(--caption);
  }

  .label {
    position: absolute; left: 244px; top: 40px;
    width: 360px; height: 460px; border-radius: 10px; overflow: hidden;
    display: flex; flex-direction: column; align-items: center;
  }

  /* Option 3 */
  .label--roast { background: var(--roast); }
  .label--roast .label__art {
    margin-top: 56px; width: 220px; height: 200px; border-radius: 90px 90px 14px 14px;
    background: linear-gradient(160deg, var(--tan) 0%, var(--amber) 70%, var(--ember) 100%);
  }
  .label--roast .label__name {
    margin-top: 10px; font: 400 62px/1 "Titan One", sans-serif; color: var(--cream);
    letter-spacing: 1px;
  }
  .label--roast .label__origin {
    margin-top: 16px; font: 400 14px "Oswald", sans-serif; letter-spacing: 6px; color: var(--cream);
  }
  .label--roast .label__weight {
    margin-top: 12px; font: 400 12px "Oswald", sans-serif; letter-spacing: 2px; color: var(--cream);
  }

  /* Option 4 */
  .label--teal { background: var(--teal); }
  .label--teal .label__frame {
    position: absolute; inset: 14px; border: 1.5px solid var(--gold); border-radius: 4px;
  }
  .label--teal .label__art {
    margin-top: 44px; width: 190px; height: 190px; border-radius: 50%;
    background: radial-gradient(circle at 62% 50%, var(--ember) 0%, var(--navy) 75%);
  }
  .label--teal .label__name {
    margin-top: 18px; font: 400 58px/1.1 "Poiret One", sans-serif; color: var(--cream);
  }
  .label--teal .label__origin {
    margin-top: 2px; font: 300 17px "Josefin Sans", sans-serif; color: var(--gold); letter-spacing: 1px;
  }
  .label--teal .label__badge {
    margin-top: 16px; padding: 6px 18px; border: 1px solid var(--gold);
    font: 400 10px "Josefin Sans", sans-serif; letter-spacing: 4px; color: var(--gold);
    text-align: center; line-height: 1.5; text-transform: uppercase;
  }
  .label--teal .label__weight {
    margin-top: 12px; font: 400 11px "Josefin Sans", sans-serif; letter-spacing: 2px; color: var(--cream);
  }
</style>
</head>
<body>
<main class="sheet">
  <section class="option option--three">
    <div class="label label--roast">
      <div class="label__art" role="img" aria-label="Illustration of a steaming orange coffee cup with a hand and red bean before a tan arch"></div>
      <h2 class="label__name">Coffee</h2>
      <p class="label__origin">CALIFORNIA</p>
      <p class="label__weight">300 g · 8.8 oz</p>
    </div>
    <p class="option__caption">Option 3</p>
  </section>

  <section class="option option--four">
    <div class="label label--teal">
      <div class="label__frame"></div>
      <div class="label__art" role="img" aria-label="Illustration of an orange crescent moon on a dark navy circle with fine rays"></div>
      <h2 class="label__name">Coffee</h2>
      <p class="label__origin">Roasted in California</p>
      <div class="label__badge">Small Batch<br>Organic</div>
      <p class="label__weight">300 g / 10 oz</p>
    </div>
    <p class="option__caption">Option 4</p>
  </section>
</main>
</body>
</html>
```